Trendy Interior Design Company Postcard

We're looking to create a 4x6 or 5x7 double sided postcard type of flyer with our Logo on the front and some photos and information on the back. We would like it to capture peoples attention and to communicate that we are a trendy interior design/build company that can take on a diverse variety of projects to suit any type of client.
We have many more photos of projects, if needed.

Target Market(s)

High end residential home renovations and builds.

Industry/Entity Type

It Company

Font styles to use
Serif
Sans Serif

Requirements
Must have
• Our logo on the front, and on the back we want a variety of photos of our jobs, We would like our company contact information: 555-238-9047 - info@quorvel.ca and something to entice potential clients to contact us, such as " Call for your quote today"
Nice to have
• Diversity in designs. As many photos as possible without looking too busy. We want it to look clean, sleek, and neat. Colours should match our website and logo.
Should not have
• Too much colour. No tacky/unprofessional looking fonts.

```html
<!DOCTYPE html>
<html lang="en">
<head>
<meta charset="utf-8">
<title>Quorvel Homes – Design | Plan | Build</title>
<link rel="stylesheet" href="https://fonts.googleapis.com/css2?family=Archivo:wght@700&family=Roboto+Condensed:wght@400;700&display=swap">
<style>
  :root {
    --ink: #111111;
    --paper: #ffffff;
    --band: #141414;
    --text: #1c1c1c;
    --frame: #1a1a1a;
  }
  * { margin: 0; padding: 0; box-sizing: border-box; }
  html, body { width: 1200px; height: 857px; overflow: hidden; background: var(--paper); }
  .postcard { position: relative; width: 1200px; height: 857px; background: var(--paper); overflow: hidden; font-family: "Roboto Condensed", "Arial Narrow", sans-serif; color: var(--text); }

  .band { position: absolute; background: var(--band); }
  .band--left { left: 0; top: 110px; width: 34px; height: 397px; }
  .band--right { left: 1166px; top: 110px; width: 34px; height: 397px; }
  .band--foot-a { left: 0; top: 663px; width: 240px; height: 194px; }
  .band--foot-b { left: 0; top: 690px; width: 634px; height: 167px; }

  .photo { position: absolute; }
  .photo--framed { border: 2px solid var(--frame); }
  .photo__label { position: absolute; left: 26px; bottom: 8px; color: #fff; font: 700 11px "Roboto Condensed", sans-serif; letter-spacing: .3px; }

  .tub { left: 46px; top: 53px; width: 168px; height: 178px; background: linear-gradient(160deg, #3a4350 0%, #2a2f38 45%, #e9ecef 60%, #bfc4ca 100%); }
  .kitchen-a { left: 229px; top: 53px; width: 229px; height: 178px; background: linear-gradient(135deg, #e8e4de 0%, #7b5a41 45%, #2b2522 80%, #a68a6c 100%); }
  .stairs-a { left: 471px; top: 53px; width: 131px; height: 178px; background: linear-gradient(170deg, #f1ede6 0%, #8b6a4d 55%, #3b2a1f 100%); }
  .house-before { left: 46px; top: 244px; width: 237px; height: 184px; background: linear-gradient(180deg, #d9dde2 0%, #6e5a4d 45%, #2e2724 65%, #f3f4f6 100%); }
  .house-after { left: 46px; top: 430px; width: 237px; height: 183px; background: linear-gradient(180deg, #4d6b3e 0%, #7d8a7c 40%, #9a9a92 70%, #3f6a2e 100%); }
  .stairs-b { left: 295px; top: 244px; width: 112px; height: 179px; background: linear-gradient(160deg, #f4f1ec 0%, #a07850 60%, #4b3423 100%); }
  .living { left: 418px; top: 244px; width: 184px; height: 179px; background: linear-gradient(135deg, #f2efe9 0%, #6f6a66 40%, #8e6440 75%, #d9d3ca 100%); }
  .kitchen-b { left: 295px; top: 433px; width: 189px; height: 180px; background: linear-gradient(170deg, #f0f0ef 0%, #c9c4bd 50%, #a88f76 100%); }
  .bath { left: 494px; top: 433px; width: 108px; height: 180px; background: linear-gradient(160deg, #dcd8d2 0%, #5e5853 55%, #2f2b28 100%); }
  .kitchen-c { left: 46px; top: 626px; width: 168px; height: 179px; background: linear-gradient(160deg, #d8d7d3 0%, #6f6f6e 45%, #1e1e1e 100%); }
  .dining { left: 229px; top: 626px; width: 133px; height: 179px; background: linear-gradient(180deg, #f0efec 0%, #b8b4ad 50%, #2c2a2a 100%); }
  .kitchen-d { left: 373px; top: 626px; width: 229px; height: 179px; background: linear-gradient(150deg, #eeece8 0%, #a7a39c 45%, #2a2625 75%, #9a948c 100%); }

  .info { position: absolute; left: 642px; top: 80px; width: 484px; }
  .info__heading { font-family: "Archivo", Arial, sans-serif; font-weight: 700; font-size: 29px; letter-spacing: .4px; text-align: center; color: var(--ink); margin-left: 20px; white-space: nowrap; }
  .info__intro { margin-top: 22px; font-size: 12.6px; line-height: 17px; }
  .benefits { list-style: none; margin-top: 3px; }
  .benefits li { position: relative; padding-left: 19px; font-size: 12.6px; line-height: 17px; margin-bottom: 7px; }
  .benefits svg { position: absolute; left: 1px; top: 4px; width: 12px; height: 10px; }

  .contact { position: absolute; left: 703px; top: 653px; color: var(--ink); }
  .contact__cta { font-size: 21px; }
  .contact__phone { font-family: "Archivo", Arial, sans-serif; font-weight: 700; font-size: 30px; margin-top: 8px; letter-spacing: .2px; }
  .contact__line { font-size: 20.5px; line-height: 23px; }
  .contact__line:first-of-type { margin-top: 6px; }

  .brand { position: absolute; left: 940px; top: 700px; width: 186px; text-align: center; }
  .brand__mark { display: block; width: 34px; height: 34px; background: var(--ink); margin: 0 auto 10px; }
  .brand__name { font-family: "Roboto Condensed", sans-serif; font-weight: 400; font-size: 20px; letter-spacing: 2px; color: var(--ink); }
</style>
</head>
<body>
<main class="postcard">
  <div class="band band--left"></div>
  <div class="band band--right"></div>
  <div class="band band--foot-a"></div>
  <div class="band band--foot-b"></div>

  <section class="gallery">
    <div class="photo tub" role="img" aria-label="Freestanding white bathtub in a dark tiled bathroom"></div>
    <div class="photo kitchen-a" role="img" aria-label="Kitchen with walnut cabinets, pendant lights and bar stools"></div>
    <div class="photo stairs-a" role="img" aria-label="Open wood staircase with glass railing"></div>
    <div class="photo photo--framed house-before" role="img" aria-label="Tudor-style house in winter before renovation"><span class="photo__label">BEFORE</span></div>
    <div class="photo photo--framed house-after" role="img" aria-label="Renovated craftsman-style house with stone porch"><span class="photo__label">AFTER</span></div>
    <div class="photo stairs-b" role="img" aria-label="Floating wood stairs beside a white wall"></div>
    <div class="photo living" role="img" aria-label="Living room with stone fireplace wall and shelving"></div>
    <div class="photo kitchen-b" role="img" aria-label="Bright kitchen island with white counter"></div>
    <div class="photo bath" role="img" aria-label="Modern bathroom with glass shower"></div>
    <div class="photo kitchen-c" role="img" aria-label="Kitchen with stainless range hood and dark counter"></div>
    <div class="photo dining" role="img" aria-label="Dining table with dark chairs"></div>
    <div class="photo kitchen-d" role="img" aria-label="Open kitchen with island, stools and wine shelf"></div>
  </section>

  <section class="info">
    <h1 class="info__heading">DESIGN &nbsp;|&nbsp; PLAN &nbsp;|&nbsp; BUILD</h1>
    <p class="info__intro">We offer a dedicated and comfortable construction experience by providing all of the following features and benefits to our clients:</p>
    <ul class="benefits">
      <li><svg viewBox="0 0 12 10"><path d="M1 5.5 L4.5 9 L11 1" fill="none" stroke="#1c1c1c" stroke-width="1.6"/></svg>Customer Login to our proprietary client site where clients can choose products, see schedules, request changes and communicate directly with the project manager.</li>
      <li><svg viewBox="0 0 12 10"><path d="M1 5.5 L4.5 9 L11 1" fill="none" stroke="#1c1c1c" stroke-width="1.6"/></svg>Dedicated, Northern-Builders-Guild-trained, Project Manager</li>
      <li><svg viewBox="0 0 12 10"><path d="M1 5.5 L4.5 9 L11 1" fill="none" stroke="#1c1c1c" stroke-width="1.6"/></svg>Regular contractor-client meetings to keep you informed and a part of the process</li>
      <li><svg viewBox="0 0 12 10"><path d="M1 5.5 L4.5 9 L11 1" fill="none" stroke="#1c1c1c" stroke-width="1.6"/></svg>Regular site visits (for those who will live elsewhere during construction)</li>
      <li><svg viewBox="0 0 12 10"><path d="M1 5.5 L4.5 9 L11 1" fill="none" stroke="#1c1c1c" stroke-width="1.6"/></svg>Integrated design services for a direct and easy connection to the designer and construction team</li>
      <li><svg viewBox="0 0 12 10"><path d="M1 5.5 L4.5 9 L11 1" fill="none" stroke="#1c1c1c" stroke-width="1.6"/></svg>Professional, clean cut and friendly staff to make you feel comfortable and connected to your project</li>
      <li><svg viewBox="0 0 12 10"><path d="M1 5.5 L4.5 9 L11 1" fill="none" stroke="#1c1c1c" stroke-width="1.6"/></svg>Pre-Construction Planning to drastically reduce stress and project delays</li>
      <li><svg viewBox="0 0 12 10"><path d="M1 5.5 L4.5 9 L11 1" fill="none" stroke="#1c1c1c" stroke-width="1.6"/></svg>This is accomplished by ensuring design choices, product selections and ordering are done at pre-set dates to accommodate for manufacturing lag times</li>
      <li><svg viewBox="0 0 12 10"><path d="M1 5.5 L4.5 9 L11 1" fill="none" stroke="#1c1c1c" stroke-width="1.6"/></svg>Professional contracts – the cornerstone of our client relationships</li>
      <li><svg viewBox="0 0 12 10"><path d="M1 5.5 L4.5 9 L11 1" fill="none" stroke="#1c1c1c" stroke-width="1.6"/></svg>Highly detailed to provide piece of mind</li>
      <li><svg viewBox="0 0 12 10"><path d="M1 5.5 L4.5 9 L11 1" fill="none" stroke="#1c1c1c" stroke-width="1.6"/></svg>Eliminate conflict between the client and the construction team allowing for a smooth and comfortable construction experience</li>
      <li><svg viewBox="0 0 12 10"><path d="M1 5.5 L4.5 9 L11 1" fill="none" stroke="#1c1c1c" stroke-width="1.6"/></svg>Ensure trust between our clients and Quorvel Homes Inc. by eliminating double billings, unwarranted charges and the guess work</li>
      <li><svg viewBox="0 0 12 10"><path d="M1 5.5 L4.5 9 L11 1" fill="none" stroke="#1c1c1c" stroke-width="1.6"/></svg>Act as a basis for warranty work</li>
      <li><svg viewBox="0 0 12 10"><path d="M1 5.5 L4.5 9 L11 1" fill="none" stroke="#1c1c1c" stroke-width="1.6"/></svg>2-year warranty on all workmanship</li>
    </ul>
  </section>

  <section class="contact">
    <p class="contact__cta">Call for your quote today</p>
    <p class="contact__phone">555-238-9047</p>
    <p class="contact__line">email: info@quorvel.ca</p>
    <p class="contact__line">web:&nbsp;&nbsp; www.quorvel.ca</p>
  </section>

  <div class="brand">
    <span class="brand__mark"></span>
    <span class="brand__name">QUORVEL HOMES</span>
  </div>
</main>
</body>
</html>
```